Moulding supply company needs a Door Hanger Design

Door Hanger Design Request from Ledge Craft
www. ledgecrafts.example
We are moulding factory outlet in Toronto. Provide high quality moulding materials with competitive price like crown mouldings, casings, wainscoting, flatstocks, baseboards. We also provide professional installation for our clients. This door hanger will help the home owner easily find a local factory supplier with providing the materials as well as installation.

Detail request for design:
Size: 4”x11”, vertical
Shape: Rectangle

Content:
Front
1. Logo, see attachment(Use the left one, horizontal one)
2. Moulding factory outlet direct sale
3. Supply high quality Crown mouldings, baseboards, casings and wainscotings with competitive price
4. Installation & delivery
#2 content is the most important content, should be bold and readable
#3 can be smaller font compare to #2

Address: 47 North Willow Vale Rd, Richmond Hill, ON L4B 3K9
Telephone: 416 555 0143
416 555 0187
Email: info@ledgecrafts.example

Back
Slogan: Convert plain room into designer’s interiors

Telephone: 416 555 0143
416 555 0187
Email: info@ledgecrafts.example

Images:
Front
1. Display our productions for crown mouldings, baseboards, casings and wainscotings, refer to our website www.ledgecrafts.example. (The winner finally we will provide the high resolution images, low resolution please copy from our website so far)
Back
2. Display 4-6 nice images for 1. wainscoting walls 2. feature walls, 3. waffle ceiling like attached below. BUT PLEASE DON'T USE THE IMAGES PROVIDED, THIS IS ONLY A SAMPLE. Please use high resolution images for printing. ALSO PLEASE DON'T LIMIT YOUR CREATIVITY TO USE 4 SQUARES LIKE BELOW IMAGES. Please provide more ideas

Note:
1. Please do the bleeding for final printing production
2. Images have to be high resolution for ready to print
3. Style need to be fresh, clean, easy to read, modern and magazine style
4. Information has to be readable, easy to find, front and back both need to display company address, telephone, email, you can use icon or abbreviation to do these information.

Thanks,
Ledge Crafts

```html
<!DOCTYPE html>
<html lang="en">
<head>
<meta charset="utf-8">
<title>Ledge Crafts – Door Hangers</title>
<link rel="stylesheet" href="https://fonts.googleapis.com/css2?family=Lato:wght@400;700;900&display=swap">
<style>
  :root {
    --stage: #231f20;
    --blue: #324c9b;
    --orange: #e8522a;
    --ink: #242424;
    --white: #ffffff;
    --panel-grey: #c9c9c9;
    --logo-grey: #6b6e72;
    --lace: #d9d9d9;
  }
  html, body {
    margin: 0;
    width: 955px;
    height: 1200px;
    overflow: hidden;
    background: var(--stage);
  }
  .hanger {
    position: absolute;
    top: 124px;
    width: 347px;
    height: 954px;
    display: block;
  }
  .hanger--front { left: 103px; }
  .hanger--back { left: 505px; }

  .hanger text { font-family: "Lato", Arial, sans-serif; }
  .headline { font-weight: 900; font-size: 88px; }
  .headline--back { font-size: 81px; }
  .ink { fill: var(--ink); }
  .accent { fill: var(--orange); }
  .light { fill: var(--white); }
  .category-label { font-weight: 700; font-size: 17px; letter-spacing: 0.5px; }
  .supply-copy { font-weight: 700; font-size: 27px; fill: var(--ink); }
  .service-tag { font-weight: 900; font-size: 22px; fill: var(--white); }
  .brand-name { font-weight: 400; font-size: 50px; fill: var(--logo-grey); letter-spacing: 3px; }
  .contact-title { font-weight: 700; font-size: 22px; fill: var(--white); }
  .contact-line { font-weight: 700; font-size: 19px; fill: var(--white); }
  .photo-label { font-weight: 700; font-size: 17px; fill: var(--white); }
</style>
</head>
<body>

<!-- FRONT -->
<svg class="hanger hanger--front" viewBox="0 0 623 1713" xmlns="http://www.w3.org/2000/svg" aria-label="Ledge Crafts door hanger, front">
  <defs>
    <linearGradient id="profileShade" x1="0" y1="0" x2="1" y2="1">
      <stop offset="0" stop-color="#f4f4f4"/>
      <stop offset="1" stop-color="#9a9a9a"/>
    </linearGradient>
    <clipPath id="frontClip"><rect width="623" height="1713"/></clipPath>
  </defs>
  <g clip-path="url(#frontClip)">
    <rect class="sheet" width="623" height="1713" fill="var(--white)"/>
    <path class="top-field" fill="var(--blue)"
      d="M0 0 H623 V938 C600 900 585 850 540 840 C480 830 460 870 400 880 C330 890 300 810 200 815 C110 820 60 850 0 862 Z"/>
    <polygon class="diagonal-band" fill="var(--white)" points="585,0 623,0 623,118 80,808 0,808 0,778"/>

    <g class="category-tiles" fill="var(--orange)" stroke="var(--blue)" stroke-width="5">
      <polygon points="153,265 315,383 200,548 35,423" stroke="none"/>
      <polygon points="490,283 650,400 515,568 365,443"/>
      <polygon points="360,448 520,568 390,733 235,608"/>
      <polygon points="225,608 390,733 260,893 105,773"/>
    </g>

    <g role="img" aria-label="Crown moulding profile sample">
      <polygon fill="url(#profileShade)" points="135,318 175,330 245,465 205,505 140,430"/>
    </g>
    <g role="img" aria-label="Baseboard profile sample">
      <polygon fill="url(#profileShade)" points="455,325 555,395 560,505 525,505 450,445"/>
    </g>
    <g role="img" aria-label="Casing profile sample">
      <polygon fill="url(#profileShade)" points="355,500 405,540 410,680 370,680 320,630"/>
    </g>
    <g role="img" aria-label="Wainscoting moulding profile sample">
      <polygon fill="url(#profileShade)" points="185,720 280,690 310,740 215,830 195,825"/>
    </g>

    <text class="category-label light" transform="translate(40,415) rotate(-51)">CROWN MOULDINGS</text>
    <text class="category-label ink" transform="translate(388,405) rotate(-51)">BASEBOARDS</text>
    <text class="category-label ink" transform="translate(265,555) rotate(-51)">CASINGS</text>
    <text class="category-label ink" transform="translate(118,737) rotate(-51)">WAINSCOTING</text>

    <circle class="hang-hole" cx="311" cy="178" r="103" fill="var(--white)"/>

    <polygon class="supply-panel" fill="var(--panel-grey)"
      points="450,1046 590,1046 590,1355 275,1355 275,1248 375,1248 375,1166 410,1166 410,1084 450,1084"/>
    <g class="supply-copy" text-anchor="end">
      <text x="580" y="1083">Supply</text>
      <text x="580" y="1121">high quality</text>
      <text x="580" y="1158">Crown</text>
      <text x="580" y="1196">mouldings,</text>
      <text x="580" y="1233">baseboards,</text>
      <text x="580" y="1271">casings and</text>
      <text x="580" y="1308">wainscotings with</text>
      <text x="580" y="1345">competitive price</text>
    </g>

    <g class="headline">
      <text class="ink" x="40" y="986" textLength="520" lengthAdjust="spacingAndGlyphs">MOULDING</text>
      <text class="accent" x="40" y="1073" textLength="418" lengthAdjust="spacingAndGlyphs">FACTORY</text>
      <text class="ink" x="40" y="1156" textLength="357" lengthAdjust="spacingAndGlyphs">OUTLET</text>
      <text class="ink" x="40" y="1236" textLength="327" lengthAdjust="spacingAndGlyphs">DIRECT</text>
      <text class="accent" x="40" y="1318" textLength="215" lengthAdjust="spacingAndGlyphs">SALE</text>
    </g>

    <polygon class="service-bar" fill="var(--blue)" points="58,1385 463,1385 435,1420 35,1420"/>
    <text class="service-tag" x="95" y="1411">INSTALLATION &amp; DELIVERY</text>

    <rect class="brand-square" x="92" y="1458" width="58" height="58" fill="var(--orange)"/>
    <text class="brand-name" x="172" y="1508">Ledge Crafts</text>

    <rect role="img" aria-label="Decorative lace border" class="lace-border" y="1555" width="623" height="18" fill="var(--lace)"/>
    <rect class="contact-bar" y="1578" width="623" height="135" fill="var(--orange)"/>
    <text class="contact-title" x="81" y="1604">CONTACT US</text>
    <line x1="225" y1="1597" x2="543" y2="1597" stroke="var(--white)" stroke-width="2"/>
    <g class="contact-icons" fill="var(--blue)">
      <circle cx="56" cy="1627" r="11"/><circle cx="56" cy="1655" r="11"/><circle cx="56" cy="1682" r="11"/>
    </g>
    <g fill="none" stroke="var(--white)" stroke-width="2">
      <path d="M51 1622 q0 8 8 10 l2 -3 l-3 -2 l-1 1 q-3 -2 -3 -4 l1 -1 l-2 -3 z"/>
      <rect x="50" y="1651" width="12" height="8"/><path d="M50 1651 l6 5 l6 -5"/>
      <circle cx="56" cy="1680" r="3"/>
    </g>
    <text class="contact-line" x="81" y="1634">416 555 0143, 416 555 0187</text>
    <text class="contact-line" x="81" y="1662">info@ledgecrafts.example</text>
    <text class="contact-line" x="81" y="1689">47 North Willow Vale Rd, Richmond Hill, ON L4B 3K9</text>
  </g>
</svg>

<!-- BACK -->
<svg class="hanger hanger--back" viewBox="0 0 623 1713" xmlns="http://www.w3.org/2000/svg" aria-label="Ledge Crafts door hanger, back">
  <defs>
    <linearGradient id="wallTone" x1="0" y1="0" x2="1" y2="1">
      <stop offset="0" stop-color="#d6d6d4"/><stop offset="1" stop-color="#9fa09e"/>
    </linearGradient>
    <linearGradient id="roomTone" x1="0" y1="0" x2="0" y2="1">
      <stop offset="0" stop-color="#eeeeec"/><stop offset="1" stop-color="#c9c7c2"/>
    </linearGradient>
    <linearGradient id="ceilingTone" x1="0" y1="0" x2="0" y2="1">
      <stop offset="0" stop-color="#e6e1d8"/><stop offset="1" stop-color="#8d8377"/>
    </linearGradient>
    <linearGradient id="gridTone" x1="0" y1="0" x2="0" y2="1">
      <stop offset="0" stop-color="#e3e3e3"/><stop offset="1" stop-color="#a3a3a3"/>
    </linearGradient>
    <clipPath id="backClip"><rect width="623" height="1713"/></clipPath>
  </defs>
  <g clip-path="url(#backClip)">
    <rect class="sheet" width="623" height="1713" fill="var(--white)"/>
    <path class="top-field" fill="var(--orange)"
      d="M0 0 H623 V880 C585 872 565 880 545 900 L300 820 C200 790 120 800 60 850 C30 875 10 910 0 945 Z"/>
    <circle class="hang-hole" cx="311" cy="178" r="103" fill="var(--white)"/>

    <g class="headline headline--back">
      <text class="ink" x="70" y="381" textLength="362" lengthAdjust="spacingAndGlyphs">CONVERT</text>
      <text class="light" x="70" y="451" textLength="485" lengthAdjust="spacingAndGlyphs">PLAIN ROOM</text>
      <text class="ink" x="70" y="523" textLength="188" lengthAdjust="spacingAndGlyphs">INTO</text>
      <text class="ink" x="70" y="593" textLength="433" lengthAdjust="spacingAndGlyphs">DESIGNER’S</text>
      <text class="light" x="70" y="666" textLength="400" lengthAdjust="spacingAndGlyphs">INTERIORS</text>
    </g>

    <g class="photo-grid">
      <rect x="50" y="698" width="36" height="235" fill="var(--blue)"/>
      <rect role="img" aria-label="Photo: stairwell with wainscoting panel walls" x="96" y="698" width="235" height="235" fill="url(#wallTone)"/>
      <rect role="img" aria-label="Photo: room with white wainscoting below a window" x="338" y="698" width="235" height="235" fill="url(#roomTone)"/>

      <rect role="img" aria-label="Photo: bedroom feature wall with diagonal trim" x="50" y="941" width="235" height="235" fill="url(#roomTone)"/>
      <rect role="img" aria-label="Photo: white grid panel feature wall" x="292" y="941" width="235" height="235" fill="url(#wallTone)"/>
      <rect x="536" y="941" width="37" height="235" fill="var(--blue)"/>

      <rect x="50" y="1186" width="36" height="235" fill="var(--blue)"/>
      <rect role="img" aria-label="Photo: coffered waffle ceiling with pendant light" x="96" y="1186" width="235" height="235" fill="url(#ceilingTone)"/>
      <rect role="img" aria-label="Photo: large grid waffle ceiling in open hall" x="338" y="1186" width="235" height="235" fill="url(#gridTone)"/>
    </g>
    <text class="photo-label" transform="translate(74,915) rotate(-90)">WAINSCOTING WALLS</text>
    <text class="photo-label" transform="translate(560,1133) rotate(-90)">FEATURE WALLS</text>
    <text class="photo-label" transform="translate(74,1410) rotate(-90)">WAFFLE CEILING</text>

    <rect class="brand-square" x="92" y="1458" width="58" height="58" fill="var(--orange)"/>
    <text class="brand-name" x="172" y="1508">Ledge Crafts</text>

    <rect role="img" aria-label="Decorative lace border" class="lace-border" y="1555" width="623" height="18" fill="var(--lace)"/>
    <rect class="contact-bar" y="1578" width="623" height="135" fill="var(--orange)"/>
    <text class="contact-title" x="81" y="1604">CONTACT US</text>
    <line x1="225" y1="1597" x2="543" y2="1597" stroke="var(--white)" stroke-width="2"/>
    <g class="contact-icons" fill="var(--blue)">
      <circle cx="56" cy="1627" r="11"/><circle cx="56" cy="1655" r="11"/><circle cx="56" cy="1682" r="11"/>
    </g>
    <g fill="none" stroke="var(--white)" stroke-width="2">
      <path d="M51 1622 q0 8 8 10 l2 -3 l-3 -2 l-1 1 q-3 -2 -3 -4 l1 -1 l-2 -3 z"/>
      <rect x="50" y="1651" width="12" height="8"/><path d="M50 1651 l6 5 l6 -5"/>
      <circle cx="56" cy="1680" r="3"/>
    </g>
    <text class="contact-line" x="81" y="1634">416 555 0143, 416 555 0187</text>
    <text class="contact-line" x="81" y="1662">info@ledgecrafts.example</text>
    <text class="contact-line" x="81" y="1689">47 North Willow Vale Rd, Richmond Hill, ON L4B 3K9</text>
  </g>
</svg>

</body>
</html>
```